Hair Extension Aftercare sheet

This sheet is to give to customers regarding the aftercare of hair extensions. There should be Simple and minimal look - approx A5 size and can be folded to suit. I have attached the content and logo files for use.
We are not looking for to much artwork just clean, professional look.
All the content provided in a compact flyer format i.e
A foldable A5 pamphlet or the like, this is for packaging requirements
Please do not submit A4 layouts

Industry/Entity Type

Hair And Beauty

Requirements
Must have
• All the content provided in a compact flyer format i.e
• A foldable A5 pamphlet or the like, this is for packaging requirements
Should not have
• tacky art work or images - must be clean lines

```html
<!DOCTYPE html>
<html lang="en">
<head>
<meta charset="utf-8">
<title>Elena Marsh Hair Extensions – Aftercare Pamphlet</title>
<link href="https://fonts.googleapis.com/css2?family=Cormorant+Garamond:wght@500&family=Lato:wght@400;700&display=swap" rel="stylesheet">
<style>
:root{
  --gold:#f2b61f;
  --gold-deep:#d99a12;
  --orange:#e8732a;
  --brown:#3b1c1e;
  --ink:#2b2b2b;
  --paper-top:#f7f7f7;
  --paper-mid:#e3e3e3;
  --bg:#eeeeee;
}
*{box-sizing:border-box;margin:0;padding:0}
html,body{width:1200px;height:998px;overflow:hidden;background:var(--bg)}
body{font-family:'Lato',Arial,sans-serif;color:var(--ink)}
.canvas{position:relative;width:1200px;height:998px}
.spread{position:absolute;left:30px;width:1140px;height:450px;display:flex;box-shadow:0 6px 18px rgba(0,0,0,.18)}
.spread--outer{top:30px}
.spread--inner{top:510px}
.page{position:relative;width:570px;height:450px;overflow:hidden;background:linear-gradient(160deg,var(--paper-top),var(--paper-mid) 60%,#f4f4f4)}
.page+.page{border-left:1px solid rgba(0,0,0,.08)}
.photo{position:absolute}
.curve{position:absolute;left:0;width:570px}
.body-copy{position:absolute;font-size:7.6px;line-height:1.38}
.body-copy p{margin-bottom:5px}
.body-copy b{font-weight:700}
.label{color:var(--orange);font-weight:700;font-size:9px;letter-spacing:.3px;margin-bottom:3px;text-transform:uppercase}
.label--caps-note{font-size:8.4px;text-transform:uppercase;margin-bottom:6px}
/* back page */
.back .photo--left{left:0;top:0;width:170px;height:150px;background:linear-gradient(135deg,#c8c8c8,#8e2a3a 70%,#5a1a22)}
.back .photo--right{left:330px;top:0;width:240px;height:150px;background:linear-gradient(135deg,#dadada,#3a3a3a 60%,#1b1b1b)}
.back .body-copy{left:26px;top:150px;width:520px}
.contact{position:absolute;left:26px;top:366px;font-size:7.4px}
.contact h3{color:var(--orange);font-size:9px;margin-bottom:6px}
.contact li{list-style:none;display:flex;align-items:center;gap:6px;margin-bottom:4px}
.contact svg{width:10px;height:10px;flex:none}
/* cover */
.cover .photo--hero{left:0;top:0;width:570px;height:245px;background:radial-gradient(ellipse at 65% 45%,#b8552a,#5a2418 45%,var(--brown) 80%)}
.brand-mini{position:absolute;left:18px;top:26px;color:#fff;font-family:'Cormorant Garamond',Georgia,serif;font-weight:500;font-size:15px;letter-spacing:3px;text-align:center}
.brand-mini span{display:block;font-size:7px;letter-spacing:3px}
.brand-mini i{display:block;width:9px;height:9px;border:1px solid #fff;margin:0 auto 4px}
.brand-main{position:absolute;left:0;width:570px;top:278px;text-align:center;font-family:'Cormorant Garamond',Georgia,serif;font-weight:500;color:#222}
.brand-main .name{font-size:40px;letter-spacing:7px}
.brand-main .sub{font-size:14px;letter-spacing:6px;margin-top:-2px}
.tagline{position:absolute;left:0;width:570px;top:352px;text-align:center;color:var(--orange);font-size:16px;line-height:1.3}
.flourish{position:absolute;top:405px;width:130px;height:32px;background:linear-gradient(90deg,transparent,rgba(217,154,18,.55),transparent);border-radius:50%}
/* inner left */
.guide-head{position:absolute;left:20px;top:22px;width:360px;height:26px;background:var(--orange);color:#fff;font-size:13px;line-height:26px;padding-left:12px;letter-spacing:.4px;border-radius:0 14px 0 0}
.circle{position:absolute;border-radius:50%;border:4px solid var(--orange)}
.circle--salon{left:430px;top:18px;width:120px;height:120px;background:linear-gradient(135deg,#f1e3d6,#b8865e)}
.circle--wash{left:18px;top:300px;width:110px;height:110px;background:linear-gradient(135deg,#d9c2a8,#6d4a35)}
.inner-left .copy-a{left:26px;top:56px;width:390px}
.inner-left .copy-b{left:26px;top:150px;width:520px}
.avoid{position:absolute;left:70px;top:268px;font-weight:700;font-size:11px}
.inner-left .copy-c{left:140px;top:290px;width:410px}
.inner-left .copy-d{left:26px;top:412px;width:520px}
/* inner right */
.inner-right .photo--styling{left:0;top:0;width:570px;height:170px;background:linear-gradient(120deg,#e9e4df,#c99a7a 55%,#6b4430)}
.inner-right .copy-a{left:26px;top:192px;width:520px}
</style>
</head>
<body>
<main class="canvas">

  <section class="spread spread--outer">
    <article class="page back">
      <div class="photo photo--left" role="img" aria-label="Photo of a woman with long red hair"></div>
      <div class="photo photo--right" role="img" aria-label="Photo of a woman with long dark hair"></div>
      <svg class="curve" style="top:95px" height="70" viewBox="0 0 570 70" aria-hidden="true">
        <path d="M0 70 L0 40 C150 -5 360 10 570 0 L570 12 C360 25 170 25 0 70Z" fill="var(--gold)"/>
        <path d="M0 70 C170 25 360 25 570 12 L570 70Z" fill="var(--paper-top)"/>
      </svg>
      <div class="body-copy">
        <p class="label">Important:</p>
        <p class="label--caps-note">Never use hot styling equipment that exceeds 200 degrees Celsius or 392 degrees Fahrenheit.</p>
        <p><b>Never brush, wash or dry the hair upside down:</b> It is important to use the right tools for maintenance. A good hair brush is a small investment to keep your hair in the best possible condition. Extension brushes with small plastic pins and real bristle hair are perfect and were specially developed for this purpose.</p>
        <p class="label">Chemical Treatments:</p>
        <p>We do not recommend to treat the hair with any chemical such as perm lotion, colouring, straightening etc. Chemical treatments make all warranties null and void. Virgin hair can be coloured because it has never been treated with chemicals. However, all warranties will be null and void.</p>
        <p><b>Colouring of Elena Marsh Hair Extensions:</b> All hair extensions (except for pure virgin hair) is processed hair. Commercial human hair is de-coloured (bleached) with chemicals prior to colour being deposited. The textures and curl patterns are created by manipulating the hydrogen bonds using extreme steam pressure. We strongly recommend you do not colour pre-coloured hair. Always test a strand before you colour all of the hair, the result is not the same as on natural hair.</p>
        <p>Our pre-lightened “B” Colours are specially created for colouring and are available in 6 colour tones. The pre-lightened “B” colours have only received one chemical treatment and have not been re-coloured. This gives you a solid base to colour the hair without causing too much damage. Although the B-series is suitable for colouring, all warranty is void when the hair is treated in any way.</p>
      </div>
      <div class="contact">
        <h3>CONTACT US</h3>
        <ul>
          <li><svg viewBox="0 0 10 10"><circle cx="5" cy="5" r="5" fill="#333"/><path d="M3 2.5l1 1-.6.8c.4.8 1 1.4 1.8 1.8l.8-.6 1 1-.7.9C4.6 7.2 2.8 5.4 2.6 3.2z" fill="#fff"/></svg>0400 123 456</li>
          <li><svg viewBox="0 0 10 10"><rect y="2" width="10" height="6.5" fill="#333"/><path d="M0 2l5 3.5L10 2" stroke="#fff" stroke-width=".8" fill="none"/></svg>hello@elenamarsh.com</li>
          <li><svg viewBox="0 0 10 10"><rect width="10" height="10" rx="2" fill="#333"/></svg>@elenamarshhair</li>
          <li><svg viewBox="0 0 10 10"><circle cx="5" cy="5" r="5" fill="#333"/></svg>elenamarsh.com/follow</li>
        </ul>
      </div>
    </article>

    <article class="page cover">
      <div class="photo photo--hero" role="img" aria-label="Portrait of a model with long curly copper hair"></div>
      <div class="brand-mini"><i></i>ELENA MARSH<span>HAIR EXTENSIONS</span></div>
      <svg class="curve" style="top:200px" height="70" viewBox="0 0 570 70" aria-hidden="true">
        <path d="M0 10 C200 55 380 30 570 20 L570 45 C380 52 200 70 0 40Z" fill="var(--gold)"/>
        <path d="M0 40 C200 70 380 52 570 45 L570 70 L0 70Z" fill="var(--paper-top)"/>
      </svg>
      <div class="brand-main"><div class="name">ELENA MARSH</div><div class="sub">HAIR EXTENSIONS</div></div>
      <p class="tagline">Our Philosophy Is Simple “ To Provide High<br>Quality, Long lasting Hair Extensions”</p>
      <div class="flourish" style="left:30px" role="img" aria-label="Gold swirl ornament"></div>
      <div class="flourish" style="left:410px" role="img" aria-label="Gold swirl ornament"></div>
    </article>
  </section>

  <section class="spread spread--inner">
    <article class="page inner-left">
      <h2 class="guide-head">AFTERCARE AND MAINTENANCE GUIDELINES</h2>
      <div class="circle circle--salon" role="img" aria-label="Photo of a stylist brushing a client's hair"></div>
      <div class="body-copy copy-a">
        <p>It is important to use the right tools for the job. A good hair brush is a small investment to keep your hair in the best possible condition and contributes to a pleasant wearing experience.</p>
        <p><b>Elena Marsh Bristle Brushes</b> with small plastic pins and real bristle hair are ideal and specially developed for this purpose. It smooths the hair without loosing brushing grip and removes tangles effortlessly.</p>
        <p><b>General:</b> Do not use oil based products, always use water dissolvable products. Oil based products will keep the hair in a wet condition and can cause matting. Oil based products attract a lot more dust and dirt which will make the hair less smooth and feel dry.</p>
      </div>
      <div class="body-copy copy-b">
        <p><b>General Washing &amp; Conditioning:</b> Shampoo at least two times per week. Never wash, brush or dry the hair upside down. Before washing, brush out all tangles with a hair extension brush. Do not use a brush with only plastic or steel pins. Always start brushing or combing at the ends, working your way up to the roots.</p>
        <p>Wet the hair thoroughly, then dispense a small amount of shampoo into your hand and rub your hands together. Apply the shampoo evenly on the scalp and at the roots. Gently wash the scalp using your fingertips without rubbing the hair. Rinse thoroughly while squeezing the hair to remove all shampoo residue. If the shampoo does not foam the first time, don't apply more shampoo but continue washing as normal. After rinsing simply re-apply the shampoo for a second time. There is no need to apply a lot of shampoo in the lengths.</p>
      </div>
      <p class="avoid">Avoid: Shampoos that contain sulphates &amp; products that are oil based.</p>
      <div class="circle circle--wash" role="img" aria-label="Photo of a client having her hair washed at a basin"></div>
      <div class="body-copy copy-c">
        <p><b>After you washed the hair:</b> After washing you may use a conditioner, apply the conditioner from the ends to half way up the length. Never at the roots. Comb the conditioner through using a large wide tooth comb until all tangles are removed. Rinse thoroughly to leave no residue. Towel dry the hair by squeezing it with the towel. Don't rub or massage the hair.</p>
        <p>You can apply small amounts of leave-in conditioner or a recommended styling product, comb through with your fingers into the direction you would like your hair to fall and scrunch it upwards once more. Let it dry naturally or use your favourite styling equipment.</p>
      </div>
      <div class="body-copy copy-d">
        <p><b>At Night:</b> Braid the hair in a large loose braid at the nape of the neck before going to sleep. Do not sleep with wet hair, this will cause tangling and will make it difficult to style the following morning.</p>
      </div>
    </article>

    <article class="page inner-right">
      <div class="photo photo--styling" role="img" aria-label="Photo of a stylist straightening a smiling client's hair"></div>
      <svg class="curve" style="top:130px" height="55" viewBox="0 0 570 55" aria-hidden="true">
        <path d="M0 55 L0 40 C200 10 400 5 570 0 L570 14 C400 18 200 28 0 55Z" fill="var(--orange)"/>
        <path d="M0 55 C200 28 400 18 570 14 L570 24 C400 28 200 40 0 55Z" fill="var(--gold)"/>
        <path d="M0 55 C200 40 400 28 570 24 L570 55Z" fill="var(--paper-top)"/>
      </svg>
      <div class="body-copy copy-a">
        <p><b>Styling the hair:</b> You can use a ceramic straightening iron or a hair dryer with a bristle brush to smooth the hair. Other styling tools that can be used are: heated rollers, steam rollers, curling irons, hot air curling tongs and setting rollers.</p>
        <p class="label">Important:</p>
        <p class="label--caps-note" style="color:var(--ink);font-weight:400;font-size:7.6px">Never use hot styling equipment that exceeds 200 degrees Celsius or 392 degrees Fahrenheit.</p>
        <p>Temperatures above this can damage the protein in the hair causing it to solidify and make the hair dry and unmanageable. Always keep hot styling equipment moving through the hair and do not hold for too long in one place. We do not recommend using straightening irons on wet hair.</p>
        <p><b>Sports and other activities:</b> Don't expose your hair to strong windy conditions like sailing, motor sports, cabriolet cars. Wear protective head wear. If you sweat a lot during work outs, at least rinse out the saltiness as this will dry out the hair.</p>
        <p><b>Visiting Saunas and steam rooms:</b> Braid the hair in a loose braid in the nape of the neck and put it up using a hair clip. The hair can get very hot and can be painful when it touches the skin just like your own natural hair. Only brush the hair when it is cooled down. Rinse the hair under the shower and condition it at the end of the visit.</p>
        <p><b>Swimming:</b> It is not recommended that you swim while wearing curly, deep curly and deep curl textures, you can swim but don't submerge your head in the water. Other textures are more suitable. Make one braid at the nape of your neck. Try to keep your hair out of the water as much as possible.</p>
        <p><b>Sunbathing:</b> Braid your hair in a large braid at the back of the neck. After sunbathing, do not undo the braid until the hair cools down.</p>
        <p><b>Tanning machines:</b> Whilst laying under a tanning machine, cover the hair loosely with a towel. Don't apply skin tan oil or sunblock to the hair.</p>
        <p><b>General Daily Styling Guide:</b> In the morning undo the braid and brush the hair starting from the ends upwards to the roots until all tangles are removed. If necessary, dampen the hair with a water spray. You can use a ceramic hair straightening iron (NOT ON DAMP OR WET HAIR) or a hair dryer with an extension brush to smooth the hair. Other styling tools that can be used are: heated rollers, steam rollers, curling irons, hot air curling tongs and setting rollers.</p>
      </div>
    </article>
  </section>

</main>
</body>
</html>
```